Wordpress Design and Coding for New Residential and Commercial Lawn and Landscape Co.

I need a Wordpress site with coding built for a startup Residential and Commercial Lawn and Landscape Company. I'm uploading our business card and logo files. I'd like a really clean design, with icons to describe services and who we serve. We don't have a lot of content being new.
We offer a large variety of services. Our 2 target customers would be residential and commercial. We offer the following services: Lawn Care and Mowing, Hedge and Shrub Trimming, Removal and Clean Up, Aeration and Sod, Mulch and Rock Installation, Landscape Installations and Renovations, and Commercial Snow Removal in the winter for Retail Shopping Centers, Communities, and other larger customers.
We serve Baltimore County, Harford County, and Surrounding areas.
Target Market(s)
We have 2 main types of customer.
1. Residential - this includes lawn maintenance, plantings, mulch & rock installs, and maintenance, etc.
2. Commercial - this includes complete care from design, planting, maintenance, etc. Communities, Property Managers, Housing Associations, Shopping Centers, Retail, etc.
Industry/Entity Type
Landscape
Coding
Coded - Design and coding required
Requirements
Must have
- Clean design. Nice distinct icons to display services and other information. Large Bold eye popping landscape photo at top.
- I've included screen shots of designs I like. Please do not copy them, they are competitors.
Nice to have
- 1. Link to our Facebook page - fb.com/brightmeadowmd
- 2. Link to FB Photos for Gallery Section - https://www.facebook.com/pg/BrightMeadowMD/photos/
- 3. Why Choose Us section.
- 4. Contact form that includes 4 sections - Name, Phone #, Service Address, and Comments.
- 5. Reviews/Testimonials on Landing Page

```html
<!DOCTYPE html>
<html lang="en">
<head>
<meta charset="utf-8">
<title>Bright Meadow Lawn &amp; Landscape</title>
<link href="https://fonts.googleapis.com/css2?family=Oswald:wght@400;500&family=Raleway:wght@400;500;600&family=Poppins:wght@300;400;500&display=swap" rel="stylesheet">
<style>
:root{
  --green:#8cb60f;
  --green-dark:#6f9408;
  --ink:#222;
  --text:#777;
  --grey-bg:#f2f2f2;
  --panel:#636363;
  --footer:#1b1b1b;
  --footer-bar:#111;
  --white:#fff;
}
*{box-sizing:border-box;margin:0;padding:0}
html,body{width:1200px;height:3098px;overflow:hidden}
body{position:relative;background:var(--white);font-family:'Poppins',sans-serif;color:var(--text)}
.abs{position:absolute}
/* top bar */
.topbar{left:0;top:0;width:1200px;height:29px;background:var(--green)}
.topbar .social{left:110px;top:7px;display:flex;gap:14px}
.topbar .social span{width:14px;height:14px;border-radius:50%;background:var(--white);opacity:.9}
.topbar .phone{right:112px;top:5px;color:var(--white);font:500 15px 'Poppins',sans-serif;display:flex;align-items:center;gap:8px}
/* header */
.header{left:0;top:29px;width:1200px;height:64px;background:var(--white)}
.logo{left:112px;top:29px;width:152px;height:100px;background:var(--white);z-index:3;display:flex;flex-direction:column;align-items:center;justify-content:center;box-shadow:0 2px 4px rgba(0,0,0,.15)}
.logo .mark{width:26px;height:26px;border-radius:50%;background:var(--green);margin-bottom:6px}
.logo .name{font:600 16px 'Raleway',sans-serif;color:var(--green);text-align:center;line-height:1.15}
.nav{right:110px;top:29px;height:64px;display:flex;align-items:center;gap:42px;font:500 11.5px 'Poppins',sans-serif;color:var(--ink)}
.nav a{color:inherit;text-decoration:none}
.nav a.active{color:var(--green)}
/* hero */
.hero{left:0;top:93px;width:1200px;height:464px;background:linear-gradient(100deg,#5a4a3a 0%,#8a7462 25%,#6e8a3c 55%,#4f7d22 100%)}
.hero-title{left:0;top:220px;width:1200px;text-align:center;color:var(--white);font:500 50px/1.1 'Oswald',sans-serif;letter-spacing:.5px}
.hero-sub{left:0;top:290px;width:1200px;text-align:center;color:var(--white);font:500 24px/1.2 'Raleway',sans-serif}
.hero-btn{left:506px;top:355px;width:188px;height:54px;border:2px solid var(--white);color:var(--white);font:500 13px 'Poppins',sans-serif;display:flex;align-items:center;justify-content:center}
/* audience */
.audience{left:112px;top:475px;width:976px;height:186px;display:flex;filter:drop-shadow(0 4px 6px rgba(0,0,0,.12))}
.aud{flex:1;display:flex;flex-direction:column;align-items:center;padding-top:22px;text-align:center}
.aud.res{background:var(--green);color:var(--white);border-radius:60px 0 0 0}
.aud.com{background:var(--white);color:var(--ink);border-radius:0 60px 60px 0}
.aud .icon{width:56px;height:56px;border-radius:50%;border:2px solid currentColor;display:flex;align-items:center;justify-content:center}
.aud.com .icon{color:var(--green)}
.aud h3{font:500 21px 'Raleway',sans-serif;letter-spacing:1px;margin-top:14px}
.aud p{font:400 12.5px/1.75 'Poppins',sans-serif;margin-top:8px;width:370px}
.aud.com p{color:var(--text)}
/* section heads */
.sec-title{left:0;width:1200px;text-align:center;font:500 36px 'Raleway',sans-serif;color:var(--ink);letter-spacing:.5px}
.sec-sub{left:0;width:1200px;text-align:center;font:400 12.5px 'Poppins',sans-serif;color:var(--text)}
/* services */
.svc{top:894px;width:310px;height:318px;border:1px solid #e2e2e2;background:var(--white);padding:52px 16px 0}
.svc.featured{background:var(--green);border-color:var(--green);color:var(--white)}
.svc h4{font:500 16px 'Raleway',sans-serif;color:var(--ink);margin-bottom:16px}
.svc.featured h4{color:var(--white)}
.svc p{font:400 12.5px/2.1 'Poppins',sans-serif}
.svc-icon{top:851px;width:86px;height:86px;border-radius:50%;background:var(--white);border:1px solid #e2e2e2;display:flex;align-items:center;justify-content:center;z-index:2}
.svc-icon.featured{background:var(--green);border-color:var(--green)}
.arrow-btn{width:28px;height:30px;background:var(--ink);display:flex;align-items:center;justify-content:center}
/* why */
.why-bg{left:0;top:1276px;width:1200px;height:719px;background:var(--grey-bg)}
.why-item{left:114px;width:480px;height:170px}
.why-item .circle{left:0;top:0;width:68px;height:68px;border-radius:50%;background:var(--green);border:4px solid #cfe39a;display:flex;align-items:center;justify-content:center}
.why-item .line{left:34px;top:68px;width:1px;height:72px;background:var(--green)}
.why-item .base{left:34px;top:140px;width:130px;height:1px;background:var(--green)}
.why-item .num{left:42px;top:122px;font:400 13px 'Poppins',sans-serif;color:var(--ink)}
.why-item h5{left:86px;top:0;font:400 16px/1.5 'Raleway',sans-serif;color:var(--ink)}
.why-item h5 span{color:var(--green);display:block}
.why-item p{left:86px;top:56px;width:390px;font:400 12px/1.75 'Poppins',sans-serif}
.why-panel{left:617px;top:1297px;width:471px;height:741px;background:var(--panel);padding:52px 44px 0;color:#eee}
.why-panel h2{font:500 33px 'Raleway',sans-serif;color:var(--white);margin-bottom:24px}
.why-panel p{font:400 11.5px/1.75 'Poppins',sans-serif;margin-bottom:16px}
.why-photo{left:659px;top:1693px;width:386px;height:296px;border:12px solid var(--white);background:linear-gradient(135deg,#4d8a2a,#9bc34f 55%,#3f6e22)}
.grass-accent{left:515px;top:1905px;width:100px;height:90px;background:linear-gradient(0deg,rgba(127,174,28,.55),rgba(127,174,28,0))}
/* testimonials */
.quote{left:300px;top:2226px;width:600px;text-align:center;font:italic 300 12px/2.25 'Poppins',sans-serif;color:#555}
.avatar{left:549px;top:2323px;width:102px;height:102px;border-radius:50%;border:4px solid var(--green);background:linear-gradient(160deg,#c8a58a,#e7d3c2)}
.who{left:0;top:2440px;width:1200px;text-align:center;font:400 12px 'Poppins',sans-serif;color:#555}
/* cta */
.cta-grass{left:0;top:2530px;width:1200px;height:241px;background:linear-gradient(180deg,rgba(255,255,255,0) 0%,#9bcb3a 30%,#5d9b1e 55%,#3f7d12 100%)}
.cta-title{left:112px;top:2664px;font:500 33px 'Raleway',sans-serif;color:var(--white)}
.cta-title b{font-weight:600}
.cta-title span{font-weight:400}
.cta-sub{left:112px;top:2712px;font:400 12.5px 'Poppins',sans-serif;color:var(--white)}
.cta-btn{left:973px;top:2690px;width:101px;height:36px;border:1.5px solid var(--white);color:var(--white);font:500 10.5px 'Poppins',sans-serif;display:flex;align-items:center;justify-content:center}
/* footer */
.footer{left:0;top:2771px;width:1200px;height:248px;background:var(--footer)}
.f-head{font:400 21px 'Raleway',sans-serif;color:#ddd;padding-bottom:10px;border-bottom:1px solid #444}
.f-links{list-style:none;margin-top:12px}
.f-links li{font:400 12px 'Poppins',sans-serif;color:#ccc;line-height:22px}
.f-links li::before{content:"›";color:#888;margin-right:10px}
.contact-row{display:flex;gap:12px;font:400 12px/1.6 'Poppins',sans-serif;color:#ddd;margin-top:12px;align-items:flex-start}
.map{left:596px;top:2853px;width:220px;height:134px;background:linear-gradient(135deg,#cfe0f0,#e8e4cf 50%,#bcd6ec);border:2px solid #fff}
.news p{font:400 12px/1.6 'Poppins',sans-serif;color:#ccc;margin:12px 0 10px}
.news .field{width:212px;height:34px;background:var(--white);font:400 11px 'Poppins',sans-serif;color:#666;padding:10px}
.news .btn{margin-top:12px;width:102px;height:34px;background:var(--green);color:var(--white);font:500 11px 'Poppins',sans-serif;display:flex;align-items:center;justify-content:center}
.bottom{left:0;top:3019px;width:1200px;height:79px;background:var(--footer-bar);border-top:1px solid #333}
.bottom .social{left:110px;top:22px;display:flex;gap:14px}
.bottom .social span{width:34px;height:34px;border-radius:50%;border:2px solid #ddd}
.bottom .copy{right:112px;top:30px;font:400 12px 'Poppins',sans-serif;color:#ccc}
</style>
</head>
<body>

<div class="abs topbar">
  <div class="abs social"><span></span><span></span><span></span><span></span></div>
  <div class="abs phone">
    <svg width="16" height="16" viewBox="0 0 24 24"><circle cx="12" cy="12" r="10" fill="none" stroke="#fff" stroke-width="2"/><path d="M8 7l2 0 1 3-1.5 1a7 7 0 0 0 3.5 3.5l1-1.5 3 1v2a1 1 0 0 1-1 1A10 10 0 0 1 7 8a1 1 0 0 1 1-1z" fill="#fff"/></svg>
    123.555.01987
  </div>
</div>

<div class="abs header"></div>
<div class="abs logo"><div class="mark"></div><div class="name">Bright Meadow<br>Lawn &amp; Landscape</div></div>
<nav class="abs nav">
  <a class="active">HOME</a><a>ABOUT US</a><a>SERVICES</a><a>TESTIMONIALS</a><a>CONTACT US</a>
</nav>

<div class="abs hero" role="img" aria-label="Landscaped garden with curved stone retaining wall, flowers and green lawn"></div>
<div class="abs hero-title">MAKE YOUR LAWN</div>
<div class="abs hero-sub">Clean &amp; Beautiful</div>
<div class="abs hero-btn">CONTACT US NOW</div>

<div class="abs audience">
  <div class="aud res">
    <div class="icon"><svg width="30" height="30" viewBox="0 0 30 30" fill="none" stroke="#fff" stroke-width="2"><path d="M4 15L15 5l11 10"/><rect x="8" y="14" width="14" height="11"/><rect x="13" y="18" width="4" height="7"/></svg></div>
    <h3>RESIDENTIAL</h3>
    <p>Lorem ipsum dolor sit amet, consectetuer adipiscing elit, sed diam nonummy nibh euismod tincidunt.</p>
  </div>
  <div class="aud com">
    <div class="icon"><svg width="30" height="30" viewBox="0 0 30 30" fill="none" stroke="#8cb60f" stroke-width="2"><rect x="6" y="8" width="8" height="17"/><rect x="16" y="4" width="8" height="21"/><path d="M3 25h24"/></svg></div>
    <h3>COMMERCIAL</h3>
    <p>Lorem ipsum dolor sit amet, consectetuer adipiscing elit, sed diam nonummy nibh euismod tincidunt.</p>
  </div>
</div>

<div class="abs sec-title" style="top:734px">FEATURED SERVICES</div>
<div class="abs sec-sub" style="top:785px">Active investment management tailored to your unique needs and goals</div>
<svg class="abs" style="left:896px;top:746px" width="12" height="16" viewBox="0 0 12 16"><path d="M9 2L3 8l6 6" fill="none" stroke="#bbb" stroke-width="2"/></svg>

<div class="abs svc-icon" style="left:123px"><svg width="40" height="40" viewBox="0 0 40 40" fill="none" stroke="#8cb60f" stroke-width="2"><path d="M6 8l10 14"/><rect x="14" y="20" width="20" height="8" rx="2"/><circle cx="17" cy="31" r="3"/><circle cx="31" cy="31" r="3"/></svg></div>
<div class="abs svc-icon featured" style="left:460px"><svg width="40" height="40" viewBox="0 0 40 40" fill="none" stroke="#fff" stroke-width="2.5"><path d="M14 6l12 24M26 6L14 30"/><circle cx="13" cy="33" r="3"/><circle cx="27" cy="33" r="3"/></svg></div>
<div class="abs svc-icon" style="left:791px"><svg width="40" height="40" viewBox="0 0 40 40" fill="none" stroke="#8cb60f" stroke-width="2"><path d="M28 8l-12 14"/><path d="M12 20l6 6-6 6-4-4z" fill="#8cb60f"/></svg></div>

<div class="abs svc" style="left:112px"><h4>Lawn Care and Mowing</h4><p>Lorem ipsum dolor sit amet, consectetuer adipiscing elit, sed diam nonummynibh euismod tincidunt ut laoreet dolore magna aliquam erat volutpat. Lorem ipsum dolor sit amet, consectetuer adipiscing elit, sed diam nonummy nibh euismod tincidunt ut laoreet dolore magna aliquam erat volutpat. Ut wisi enim ad minim veniam.</p></div>
<div class="abs svc featured" style="left:446px"><h4>Hedge &amp; Shrub Trimming</h4><p>Lorem ipsum dolor sit amet, consectetuer adipiscing elit, sed diam nonummynibh euismod tincidunt ut laoreet dolore magna aliquam erat volutpat. Lorem ipsum dolor sit amet, consectetuer adipiscing elit, sed diam nonummy nibh euismod tincidunt ut laoreet dolore magna aliquam erat volutpat. Ut wisi enim ad minim veniam.</p></div>
<div class="abs svc" style="left:779px"><h4>Leaf Removal &amp; Clean Up</h4><p>Lorem ipsum dolor sit amet, consectetuer adipiscing elit, sed diam nonummynibh euismod tincidunt ut laoreet dolore magna aliquam erat volutpat. Lorem ipsum dolor sit amet, consectetuer adipiscing elit, sed diam nonummy nibh euismod tincidunt ut laoreet dolore magna aliquam erat volutpat. Ut wisi enim ad minim veniam.</p></div>

<div class="abs arrow-btn" style="left:66px;top:1044px"><svg width="10" height="12" viewBox="0 0 10 12"><path d="M7 1L2 6l5 5" fill="none" stroke="#fff" stroke-width="2"/></svg></div>
<div class="abs arrow-btn" style="left:1106px;top:1044px"><svg width="10" height="12" viewBox="0 0 10 12"><path d="M3 1l5 5-5 5" fill="none" stroke="#fff" stroke-width="2"/></svg></div>

<div class="abs why-bg"></div>

<div class="abs why-item" style="top:1386px">
  <div class="abs circle"><svg width="28" height="28" viewBox="0 0 28 28" fill="#fff"><path d="M14 3l7 10h-4l5 7H6l5-7H7z"/><rect x="13" y="20" width="2" height="5"/></svg></div>
  <div class="abs line"></div><div class="abs base"></div><div class="abs num">01</div>
  <h5 class="abs">We are Professional<span>Landscapist</span></h5>
  <p class="abs">Lorem ipsum dolor sit amet, consectetuer adipiscing elit, sed diam nonummy nibh euismod tincidunt ut laoreet dolore magna aliquam erat volutpat.</p>
</div>
<div class="abs why-item" style="top:1576px">
  <div class="abs circle"><svg width="28" height="28" viewBox="0 0 28 28" fill="none" stroke="#fff" stroke-width="2.5"><circle cx="14" cy="14" r="10"/><path d="M9 14l4 4 7-8"/></svg></div>
  <div class="abs line"></div><div class="abs base"></div><div class="abs num">02</div>
  <h5 class="abs">Quality &amp; Reliability<span>Work</span></h5>
  <p class="abs">Lorem ipsum dolor sit amet, consectetuer adipiscing elit, sed diam nonummy nibh euismod tincidunt ut laoreet dolore magna aliquam erat volutpat.</p>
</div>
<div class="abs why-item" style="top:1774px">
  <div class="abs circle"><svg width="30" height="30" viewBox="0 0 30 30" fill="none" stroke="#fff" stroke-width="2.2"><path d="M3 14l6-5 6 4 6-4 6 5-10 8z"/></svg></div>
  <div class="abs line"></div><div class="abs base"></div><div class="abs num">03</div>
  <h5 class="abs">100 % Trusted<span>Team Member</span></h5>
  <p class="abs">Lorem ipsum dolor sit amet, consectetuer adipiscing elit, sed diam nonummy nibh euismod tincidunt ut laoreet dolore magna aliquam erat volutpat.</p>
</div>
<div class="abs grass-accent" role="img" aria-label="Decorative grass accent"></div>

<div class="abs why-panel">
  <h2>WHY CHOOSE US</h2>
  <p>Lorem ipsum dolor sit amet, consectetuer adipiscing elit, sed diam nonummy nibh euismod tincidunt ut laoreet dolore magna aliquam erat volutpat.</p>
  <p>Ut wisi enim ad minim veniam, quis nostrud exerci tation ullamcorper suscipit lobortis nisl ut aliquip ex ea commodo consequat. Duis autem vel eum iriure dolor in hendrerit in vulputate esse molestie consequat, vel illum dolore eu feugiat nulla facilisis at vero eros et accumsan. Ut wisi enim ad minim veniam, quis nostrud exerci tation ullamcorper suscipit lobortis nisl ut aliquip ex ea commodo consequat. Duis autem vel eum iriure dolor in hendrerit in vulputate esse molestie consequat, vel illum dolore eu feugiat nulla facilisis at vero eros et accumsan.</p>
</div>
<div class="abs why-photo" role="img" aria-label="Gardener kneeling among green shrubs in a garden"></div>

<div class="abs sec-title" style="top:2113px">TESTIMONIALS</div>
<div class="abs sec-sub" style="top:2164px">Active investment management tailored to your unique needs and goals</div>
<svg class="abs" style="left:112px;top:2290px" width="30" height="64" viewBox="0 0 30 64"><path d="M28 2L2 32l26 30" fill="none" stroke="#ddd" stroke-width="2"/></svg>
<svg class="abs" style="left:1058px;top:2290px" width="30" height="64" viewBox="0 0 30 64"><path d="M2 2l26 30L2 62" fill="none" stroke="#ddd" stroke-width="2"/></svg>
<div class="abs quote">“ Renewa Cell Therapy provides Embryonic Stem Cells and unique protocols to doctors in order to help their patients who face major health conditions as well as individuals who simply wish to stay young and healthy. Over the past five years of development. ”</div>
<div class="abs avatar" role="img" aria-label="Portrait photo of a client"></div>
<div class="abs who">Miss. Patient Name</div>

<div class="abs cta-grass" role="img" aria-label="Close-up of green grass blades against white"></div>
<div class="abs cta-title"><b>LEARN HOW -TO</b> <span>KEEP YOUR LAWN GREEN</span></div>
<div class="abs cta-sub">Lorem Ipsum,&nbsp; we don't agree.</div>
<div class="abs cta-btn">KNOW MORE</div>

<div class="abs footer"></div>
<div class="abs" style="left:112px;top:2816px;width:162px">
  <div class="f-head">Quick Links</div>
  <ul class="f-links"><li>Home</li><li>About</li><li>Services</li><li>Testimonials</li><li>Contact</li></ul>
</div>
<div class="abs" style="left:346px;top:2816px;width:470px">
  <div class="f-head">Contact Detail</div>
  <div class="contact-row"><svg width="14" height="16" viewBox="0 0 14 16"><path d="M7 1a5 5 0 0 1 5 5c0 4-5 9-5 9S2 10 2 6a5 5 0 0 1 5-5z" fill="#fff"/><circle cx="7" cy="6" r="2" fill="#1b1b1b"/></svg><span>Lorem Ipsum, 1820 Oak Hollow<br>Lane, Fallston, MD, 1234</span></div>
  <div class="contact-row" style="margin-top:16px"><svg width="14" height="14" viewBox="0 0 24 24"><path d="M5 3h4l2 5-2.5 1.5a11 11 0 0 0 6 6L16 13l5 2v4a2 2 0 0 1-2 2A17 17 0 0 1 3 5a2 2 0 0 1 2-2z" fill="#fff"/></svg><span style="font-size:13px">123.555.01987</span></div>
  <div class="contact-row" style="margin-top:12px"><svg width="14" height="12" viewBox="0 0 14 12"><rect x="1" y="1" width="12" height="10" fill="none" stroke="#fff" stroke-width="1.5"/><path d="M1 1l6 5 6-5" fill="none" stroke="#fff" stroke-width="1.5"/></svg><span>info@brightmeadowmd.com</span></div>
</div>
<div class="abs map" role="img" aria-label="Map showing the business location"></div>
<div class="abs news" style="left:876px;top:2816px;width:212px">
  <div class="f-head">Newsletter Sign Up</div>
  <p>Stay connected and receive email updates from Us</p>
  <div class="field">Enter your email here</div>
  <div class="btn">SUBSCRIBE</div>
</div>

<div class="abs bottom">
  <div class="abs social"><span></span><span></span><span></span><span></span><span></span></div>
  <div class="abs copy">Copyright © 2018 BrightMeadowmd.com.&nbsp; All Rights Reserved</div>
</div>

</body>
</html>
```